Harbour Loop Recycling Centre

‘HELP! Stop toxic landfill pollution’
Australians are addicted to all forms new electronic equipment, we consume more per head of population than any country on the Planet!On average we now ditch a television each 2 years, we purchase the latest smart phone every year, the latest computer each year, SME’s and large corporation companies change IT hardware each 12 months. We purchased 17 million items new electronic purchases in 2011! The kicker is: (only 2.4 million) were correctly recycled.
If you are rolling over your IT Hardware, phones, or printers think first harbour Loop Recycling, for a small fee we will correctly recycle your old E-Waste.
World standard ISO 14001.

‘TOGETHER WE CAN MAKE A DIFFERENCE’
THE NEW HARBOUR LOOP RECYCLING CENTRE
47 Corley St Brenmoor
Opening hours: 8am – 4.pm Week days and 9am – midday Saturdays.
www.harbourlooprecycling.example.au
1300 58 26 91

```html
<!DOCTYPE html>
<html lang="en">
<head>
<meta charset="utf-8">
<title>Harbour Loop Recycling Centre – Stop toxic landfill pollution</title>
<link href="https://fonts.googleapis.com/css2?family=Arimo:wght@400;700&display=swap" rel="stylesheet">
<style>
  :root {
    --paper: #ffffff;
    --lime: #b5cf52;
    --forest: #335e4a;
    --leaf: #3fae49;
    --rule: #1d1d1b;
    --sky: #5b86c8;
    --night: #22384a;
    --moss: #7fa45c;
    --text-light: #ffffff;
  }
  * { margin: 0; padding: 0; box-sizing: border-box; }
  html, body { width: 855px; height: 1200px; overflow: hidden; background: var(--paper); }
  body { font-family: "Arimo", Arial, sans-serif; }

  .poster {
    position: relative;
    width: 855px;
    height: 1200px;
    background: var(--paper);
  }
  .poster__frame {
    position: absolute;
    left: 14px; top: 14px;
    width: 827px; height: 1172px;
    overflow: hidden;
    background: var(--lime);
  }

  .hero-image {
    position: absolute;
    left: 0; top: 0;
    width: 100%; height: 620px;
    background: linear-gradient(180deg,
      var(--sky) 0%,
      var(--night) 30%,
      #3b5f5c 50%,
      var(--moss) 72%,
      var(--lime) 100%);
  }

  .headline {
    position: absolute;
    left: 0; width: 100%;
    text-align: center;
    color: var(--forest);
    font-weight: 700;
    line-height: 1;
    white-space: nowrap;
  }
  .headline--shout { top: 566px; font-size: 92px; }
  .headline--sub { top: 647px; font-size: 47px; }

  .offer {
    position: absolute;
    left: 90px; top: 751px;
    width: 647px; height: 153px;
  }
  .offer__shape { position: absolute; inset: 0; }
  .offer__body {
    position: absolute;
    left: 44px; right: 44px; top: 17px;
    text-align: center;
    color: var(--text-light);
    font-size: 17px;
    line-height: 23px;
  }
  .offer__standard {
    margin-top: 20px;
    font-weight: 700;
  }

  .footer-rule {
    position: absolute;
    left: 0; top: 930px;
    width: 100%; height: 9px;
    background: var(--rule);
  }
  .footer {
    position: absolute;
    left: 0; top: 939px;
    width: 100%; height: 233px;
    background: var(--forest);
    color: var(--text-light);
    text-align: center;
  }
  .footer__slogan {
    margin-top: 32px;
    font-size: 27px;
    line-height: 30px;
    font-weight: 700;
    white-space: nowrap;
  }
  .footer__centre {
    margin-top: 31px;
    font-size: 19px;
    line-height: 23px;
    font-weight: 700;
  }
  .footer__details {
    font-size: 19px;
    line-height: 22.5px;
    font-style: normal;
  }
</style>
</head>
<body>
  <main class="poster">
    <div class="poster__frame">
      <div class="hero-image" role="img" aria-label="Photo area: close-up of a glowing pixel display with leaf shapes"></div>

      <h1 class="headline headline--shout">HELP!</h1>
      <h2 class="headline headline--sub">Stop toxic landfill pollution</h2>

      <section class="offer">
        <svg class="offer__shape" viewBox="0 0 647 153" width="647" height="153" aria-hidden="true">
          <path d="M4 6 L642 4 L644 140 L4 140 Z" fill="var(--leaf)"/>
          <path d="M0 4 L638 0 L636 150 Q320 134 6 153 Z" fill="var(--forest)"/>
        </svg>
        <div class="offer__body">
          <p>If you are rolling over your IT Hardware, phones, or printers think first harbour Loop Recycling, for a small fee we will correctly recycle your old E-Waste.</p>
          <p class="offer__standard">World standard ISO 14001</p>
        </div>
      </section>

      <div class="footer-rule"></div>
      <footer class="footer">
        <p class="footer__slogan">“TOGETHER WE CAN MAKE A DIFFERENCE”</p>
        <p class="footer__centre">THE NEW HARBOUR LOOP RECYCLING CENTRE</p>
        <address class="footer__details">
          47 Corley St Brenmoor<br>
          Opening hours: 8am – 4.pm Week days and 9am – midday Saturdays.<br>
          www.harbourlooprecycling.example.au<br>
          1300 58 26 91
        </address>
      </footer>
    </div>
  </main>
</body>
</html>
```